Kelvar Systems Website

Website design for our company: Kelvar Systems.
The website should look fresh and IT focused. Please have a look at http://www.kelvarsystems.net.au/ for our current design. We want something fresh and new, professional looking, in WordPress so we can easily make changes.

Industry/Entity Type

It Company

```html
<!DOCTYPE html>
<html lang="en">
<head>
<meta charset="utf-8">
<title>Kelvar Systems</title>
<link rel="stylesheet" href="https://fonts.googleapis.com/css2?family=Ubuntu:wght@400;500&family=Arimo:wght@400;700&display=swap">
<style>
:root{
  --blue:#0b68c0;
  --green:#0aa84f;
  --band:#c9c9c9;
  --light:#f2f2f2;
  --dark:#1d1d1d;
  --text:#333;
  --muted:#8a8a8a;
  --line:#bdbdbd;
}
*{margin:0;padding:0;box-sizing:border-box}
html,body{width:1148px;height:1200px;overflow:hidden;background:#fff}
body{position:relative;font-family:"Arimo",Arial,sans-serif;color:var(--text)}
.abs{position:absolute}
.brand{left:170px;top:21px;height:73px;display:flex;align-items:center;gap:10px}
.brand-mark{width:22px;height:22px;background:var(--green)}
.brand-name{font-family:"Ubuntu",sans-serif;font-weight:500;font-size:26px;color:var(--green)}
.phone{left:842px;top:28px;display:flex;align-items:center;gap:6px;font-family:"Ubuntu",sans-serif;font-weight:500;font-size:19px;color:#111}
.search{left:809px;top:68px;width:178px;height:25px;border:1px solid #ccc;font-size:11px;font-style:italic;color:#555;padding:5px 8px}
.search svg{position:absolute;right:7px;top:5px}
.band{left:0;top:112px;width:1148px;height:358px;background:var(--band)}
.nav{left:160px;top:112px;width:828px;height:38px;background:var(--blue);display:flex}
.nav a{display:flex;align-items:center;justify-content:center;color:#fff;text-decoration:none;font-family:"Ubuntu",sans-serif;font-weight:500;font-size:13.5px;border-left:1px solid rgba(255,255,255,.15)}
.nav a.on{background:var(--green);border-left:0}
.hero{left:160px;top:150px;width:828px;height:364px;background:linear-gradient(110deg,#4c4f55 0%,#d8dadc 35%,#b7bcc4 55%,#8b3a34 68%,#5f78a8 82%,#c9ccd0 100%)}
.hero-arrow{position:absolute;top:132px;width:34px;height:34px;border-radius:50%;background:rgba(0,0,0,.6);display:flex;align-items:center;justify-content:center}
.caption{left:160px;top:470px;width:828px;height:44px;background:rgba(11,104,192,.85);color:#fff;font-family:"Ubuntu",sans-serif;font-size:22px;text-align:center;line-height:44px}
h2{font-family:"Ubuntu",sans-serif;font-weight:500;font-size:22px;color:var(--blue)}
h2 span{color:var(--green)}
.rule{height:1px;background:var(--line)}
.about{left:170px;top:540px;width:524px}
.about .rule{margin:5px 0 10px}
.about-text{font-size:10.5px;line-height:16px;text-align:justify;color:#333}
.about-photo{float:left;width:243px;height:112px;margin:0 15px 2px 0;background:linear-gradient(120deg,#c8b7a4,#f1efea 45%,#2c3244 70%,#e6e1d8)}
.more{font-size:11px;color:var(--green);text-align:right;margin-top:3px}
.vdiv{left:713px;top:578px;width:1px;height:172px;background:#ddd}
.services{left:730px;top:541px;width:249px}
.services .rule{margin-top:5px}
.svc{position:absolute;left:4px;display:flex;align-items:center;gap:14px;font-family:"Ubuntu",sans-serif;font-size:16px;color:#222}
.svc svg{width:32px;height:28px}
.light{left:0;top:808px;width:1148px;height:160px;background:var(--light)}
.clients{left:169px;top:834px;width:540px}
.clients .rule{margin-top:6px}
.carr{position:absolute;right:6px;top:6px;display:flex;gap:10px}
.logos{left:169px;top:890px;width:540px;display:flex;justify-content:space-between;align-items:center}
.logos span{font-family:"Ubuntu",sans-serif;font-weight:500;font-size:19px;color:#666}
.remote{left:728px;top:836px;width:251px}
.remote .rule{margin-top:6px}
.code{left:728px;top:875px;width:245px;height:25px;background:#fff;border:1px solid #ccc;font-size:10.5px;font-style:italic;color:#777;padding:6px 9px}
.btn{left:729px;top:908px;width:88px;height:21px;background:var(--green);color:#fff;font-family:"Ubuntu",sans-serif;font-size:12.5px;text-align:center;line-height:21px}
.footer{left:0;top:968px;width:1148px;height:198px;background:var(--dark);color:#ccc}
.fh{position:absolute;top:16px;font-family:"Ubuntu",sans-serif;font-size:13px;color:#fff}
.fdiv{position:absolute;top:30px;width:1px;height:150px;background:#444}
.links{position:absolute;left:169px;top:40px;width:116px;list-style:none}
.links li{height:20.3px;border-bottom:1px solid #3b3b3b;font-size:10.5px;color:#bbb;padding:3px 0 0 13px;position:relative}
.links li:last-child{border:0}
.links li::before{content:"";position:absolute;left:0;top:7px;border:3px solid transparent;border-left:4px solid #999}
.quote{position:absolute;left:324px;top:46px;width:273px;font-size:11px;line-height:15.3px;color:#bbb}
.who{position:absolute;left:324px;top:132px;width:273px;text-align:right;font-size:11px;font-weight:700;color:#aaa;line-height:14px}
.ci{position:absolute;left:652px;display:flex;gap:10px;font-size:10.5px;line-height:14px;color:#ddd}
.ci i{width:19px;height:19px;border-radius:50%;background:var(--blue);flex:none;display:flex;align-items:center;justify-content:center}
.soc{position:absolute;top:42px;width:26px;height:26px;border-radius:50%;background:#3b3b3b}
.soc.on{background:var(--green)}
.fbrand{position:absolute;left:849px;top:94px;display:flex;align-items:center;gap:7px}
.fbrand .brand-mark{width:16px;height:16px}
.fbrand .brand-name{font-size:17px}
.bottom{left:0;top:1166px;width:1148px;height:34px;background:var(--blue);color:#fff;font-size:10.5px;text-align:center;line-height:34px}
</style>
</head>
<body>

<header>
  <div class="abs brand"><div class="brand-mark"></div><div class="brand-name">Kelvar Systems</div></div>
  <div class="abs phone">
    <svg width="20" height="20" viewBox="0 0 20 20"><circle cx="10" cy="10" r="9" fill="none" stroke="#0b68c0" stroke-width="1.6"/><path d="M7 5c-1 1-1 3 1 6s4 4 5 3l-1.5-2-1.5.8-2-3 .8-1.5z" fill="#0b68c0"/></svg>
    015-482-7730
  </div>
  <div class="abs search">search
    <svg width="14" height="14" viewBox="0 0 14 14"><circle cx="6" cy="6" r="4.3" fill="none" stroke="#999" stroke-width="1.6"/><path d="M9 9l4 4" stroke="#999" stroke-width="2"/></svg>
  </div>
</header>

<div class="abs band"></div>
<nav class="abs nav">
  <a class="on" style="width:93px">HOME</a>
  <a style="width:121px;border-left:0">ABOUT US</a>
  <a style="width:113px">SERVICES</a>
  <a style="width:116px">SUPPORT</a>
  <a style="width:146px">TESTIMONIALS</a>
  <a style="width:107px">CLIENTS</a>
  <a style="width:132px">CONTACT US</a>
</nav>

<div class="abs hero" role="img" aria-label="Two engineers examining equipment in a server room">
  <div class="hero-arrow" style="left:14px"><svg width="10" height="16"><path d="M8 1L2 8l6 7" fill="none" stroke="#fff" stroke-width="1.6"/></svg></div>
  <div class="hero-arrow" style="right:10px"><svg width="10" height="16"><path d="M2 1l6 7-6 7" fill="none" stroke="#fff" stroke-width="1.6"/></svg></div>
</div>
<div class="abs caption">WE HAVE SPECIALISED ENGINEERS, TRAINED TO DO SPECIALISED WORK</div>

<section class="abs about">
  <h2>About <span>Kelvar Systems</span></h2>
  <div class="rule"></div>
  <div class="about-text">
    <div class="about-photo" role="img" aria-label="Business team meeting around a table"></div>
    Kelvar Systems is an Adelaide based company with a single objective - to excel in the support and service of all computer and IT needs. Our core business includes information technology consultation, equipment and software optimisation, network system and application software system construction, overall system network routine maintenance and management. We are currently supporting over 200 businesses through a variety of service level agreements and support plans. We provide a high level consulting service using the most experienced engineers at a reasonable and fair price. We believe in using a Business Value approach to every aspect of computer consultation to provide our clients with the most cost-effective solutions. We understand that no one business is the same and our IT service can be tailored to fit individual requirements.
  </div>
  <div class="more">Read More...</div>
</section>

<div class="abs vdiv"></div>

<section class="abs services">
  <h2>Our <span>Services</span></h2>
  <div class="rule"></div>
  <div class="svc" style="top:45px"><svg viewBox="0 0 32 28"><path d="M5 5l20 18M25 5L8 22" stroke="#333" stroke-width="3.5" stroke-linecap="round"/></svg>ON-SITE SERVICE</div>
  <div class="svc" style="top:84px"><svg viewBox="0 0 32 28"><rect x="3" y="3" width="20" height="14" fill="none" stroke="#333" stroke-width="1.8"/><path d="M10 21h8" stroke="#333" stroke-width="1.8"/><circle cx="24" cy="19" r="6" fill="#fff" stroke="#333" stroke-width="1.6"/></svg>REMOTE DESKTOP</div>
  <div class="svc" style="top:126px"><svg viewBox="0 0 32 28"><path d="M4 3v8a7 7 0 0 0 14 0V3M11 18v4a5 5 0 0 0 10 0v-6" fill="none" stroke="#333" stroke-width="1.8"/><circle cx="23" cy="11" r="4" fill="none" stroke="#333" stroke-width="1.8"/></svg>MEDICAL IT SERVICE</div>
  <div class="svc" style="top:168px"><svg viewBox="0 0 32 28"><rect x="3" y="3" width="22" height="16" fill="none" stroke="#333" stroke-width="1.8"/><path d="M7 14l5-5 4 4 5-6" fill="none" stroke="#333" stroke-width="1.5"/><circle cx="24" cy="20" r="4" fill="#fff" stroke="#333" stroke-width="1.6"/><path d="M27 23l3 3" stroke="#333" stroke-width="2"/></svg>PHARMACY IT SERVICE</div>
  <div class="svc" style="top:208px"><svg viewBox="0 0 32 28"><rect x="3" y="5" width="24" height="16" fill="none" stroke="#333" stroke-width="1.8"/><path d="M12 25h8M14 15l12-12" stroke="#333" stroke-width="1.8"/></svg>WEBSITE DESIGN</div>
  <div class="more" style="position:absolute;top:235px;right:4px">View All...</div>
</section>

<div class="abs light"></div>
<section class="abs clients">
  <h2>Our <span>Clients</span></h2>
  <div class="carr">
    <svg width="8" height="14"><path d="M7 1L1 7l6 6" fill="none" stroke="#555" stroke-width="1.4"/></svg>
    <svg width="8" height="14"><path d="M1 1l6 6-6 6" fill="none" stroke="#0aa84f" stroke-width="1.4"/></svg>
  </div>
  <div class="rule"></div>
</section>
<div class="abs logos"><span>Norvane</span><span>Quillstack</span><span>Brantel</span><span>Ostrix</span></div>

<section class="abs remote">
  <h2>Remote <span>Support</span></h2>
  <div class="rule"></div>
</section>
<div class="abs code">Enter your 6 digit code</div>
<div class="abs btn">Connect Now</div>

<footer class="abs footer">
  <div class="fh" style="left:169px">Main Links</div>
  <ul class="links"><li>Home</li><li>About Us</li><li>Services</li><li>Support</li><li>Testimonials</li><li>Clients</li><li>Contact</li></ul>
  <div class="fdiv" style="left:295px"></div>

  <div class="fh" style="left:324px">Testimonials</div>
  <div style="position:absolute;left:577px;top:20px;display:flex;gap:8px">
    <svg width="7" height="11"><path d="M6 1L1 5.5 6 10" fill="none" stroke="#ccc" stroke-width="1.3"/></svg>
    <svg width="7" height="11"><path d="M1 1l5 4.5L1 10" fill="none" stroke="#ccc" stroke-width="1.3"/></svg>
  </div>
  <p class="quote"><b style="color:#fff">“</b> I have always found the team extremely helpful with their advice over the phone. They also have the ability to access our computers remotely, and can rectify most problems quite swiftly. I have no hesitation in recommending Kelvar Systems for all of your IT needs. <b style="color:#fff">”</b></p>
  <p class="who">Daniel Werrick B.Pharm<br>Harbourline Chemists, Elder Park</p>
  <div class="fdiv" style="left:625px"></div>

  <div class="fh" style="left:652px">Contact Info</div>
  <div class="ci" style="top:42px"><i><svg width="10" height="10"><path d="M5 1L1 5h1.5v4h5V5H9z" fill="#fff"/></svg></i><span>218 Coastal Road<br>Seaview East<br>5019 Australia</span></div>
  <div class="ci" style="top:96px;align-items:center"><i><svg width="10" height="10"><path d="M2 1c-1 1 0 4 2 6s4 3 5 2L8 7 6.5 7.5 3 4 3.5 2.5z" fill="#fff"/></svg></i><span>087-114-5920</span></div>
  <div class="ci" style="top:130px;align-items:center"><i><svg width="11" height="8"><rect x=".5" y=".5" width="10" height="7" fill="#fff"/><path d="M.5 .5l5 4 5-4" fill="none" stroke="#0b68c0"/></svg></i><span>support@kelvarsystems.com</span></div>
  <div class="fdiv" style="left:821px"></div>

  <div class="fh" style="left:851px">Follow Us On</div>
  <div class="soc on" style="left:851px" aria-label="Social profile"></div>
  <div class="soc" style="left:883px" aria-label="Social profile"></div>
  <div class="soc" style="left:914px" aria-label="Social profile"></div>
  <div class="soc" style="left:945px" aria-label="Social profile"></div>
  <div class="fbrand"><div class="brand-mark"></div><div class="brand-name">Kelvar Systems</div></div>
</footer>

<div class="abs bottom">Copyright 2014 Kelvar Systems &nbsp;|&nbsp; Terms of Use &nbsp;|&nbsp; Privacy Statement &nbsp;|&nbsp; Feedback &nbsp;|&nbsp; Legal</div>

</body>
</html>
```